Number of Pages Required

1 page

Requirements
Must have
• An Overview / Background of the Business & Services(not for profit rescue animal farm)
• The Target Market / Audience you are trying to reach (animal lovers)
• Design Specifics; any preferences or ideas for Style, Colour, Imagery, etc (no preferences)

```html
<!DOCTYPE html>
<html lang="en">
<head>
<meta charset="utf-8">
<title>Animal Lover</title>
<link href="https://fonts.googleapis.com/css2?family=Courgette&family=Roboto:wght@400;700&family=Nunito+Sans:wght@400&display=swap" rel="stylesheet">
<style>
  :root {
    --hero-bg: #7f7880;
    --hero-rule: #a8a2a9;
    --white: #ffffff;
    --nav-bg: #ff5253;
    --nav-active: #00a07b;
    --page-bg: #f2f2f2;
    --ink: #0a0a0a;
    --rule-dark: #bdbdbd;
    --brand: #2aa8e0;
    --tag: #555055;
  }
  * { margin: 0; padding: 0; box-sizing: border-box; }
  html, body { width: 1200px; height: 1000px; overflow: hidden; }
  body { position: relative; background: var(--page-bg); font-family: "Roboto", sans-serif; }

  .hero { position: absolute; left: 0; top: 0; width: 1200px; height: 695px; background: var(--hero-bg); }
  .hero-rule { position: absolute; left: 0; width: 1200px; height: 1px; background: var(--hero-rule); }
  .hero-rule.top { top: 26px; }
  .hero-rule.bottom { top: 668px; }

  .brand { position: absolute; left: 165px; top: 132px; display: flex; align-items: center; gap: 8px; }
  .brand-mark { width: 18px; height: 18px; border-radius: 50%; background: var(--brand); }
  .brand-name { font-family: "Roboto", sans-serif; font-weight: 700; font-size: 22px; color: var(--brand); letter-spacing: 0.3px; }
  .brand-tag { position: absolute; left: 165px; top: 167px; font-size: 10px; letter-spacing: 8px; color: var(--tag); }

  .hero-title { position: absolute; left: 0; width: 1245px; top: 228px; text-align: center; font-family: "Courgette", cursive; font-size: 128px; color: var(--white); line-height: 1.1; }
  .hero-sub { position: absolute; left: 0; width: 1200px; top: 409px; text-align: center; font-size: 31px; color: var(--white); }

  .divider { position: absolute; left: 502px; width: 195px; height: 1px; }
  .divider.light { top: 468px; background: var(--white); }
  .divider.dark { top: 932px; background: var(--rule-dark); }
  .divider-icon { position: absolute; left: 86px; top: -12px; width: 24px; height: 22px; border-radius: 50% 50% 40% 40%; }
  .divider.light .divider-icon { background: var(--white); }
  .divider.dark .divider-icon { background: var(--ink); }

  .main-nav { position: absolute; left: 0; top: 695px; width: 1200px; height: 60px; background: var(--nav-bg); }
  .main-nav ul { list-style: none; display: flex; position: absolute; left: 165px; top: 0; height: 60px; }
  .main-nav li { height: 60px; line-height: 60px; padding: 0 16px; margin-right: 17px; font-family: "Nunito Sans", sans-serif; font-size: 15px; color: var(--white); }
  .main-nav li.active { background: var(--nav-active); margin-right: 9px; }

  .section-title { position: absolute; left: 0; width: 1200px; top: 843px; text-align: center; font-family: "Courgette", cursive; font-size: 58px; color: var(--ink); line-height: 1.1; }
</style>
</head>
<body>
  <header class="hero">
    <div class="hero-rule top"></div>
    <div class="brand">
      <span class="brand-mark"></span>
      <span class="brand-name">MEADOWBROOK RESCUE</span>
    </div>
    <div class="brand-tag">A RESCUE FARM</div>
    <h1 class="hero-title">Animal Lover</h1>
    <p class="hero-sub">WE SHOULD LOVE ANIMALS</p>
    <div class="divider light"><span class="divider-icon" role="img" aria-label="Small sitting cat silhouette"></span></div>
    <div class="hero-rule bottom"></div>
  </header>

  <nav class="main-nav">
    <ul>
      <li class="active">Home</li>
      <li>About Us</li>
      <li>Our Story</li>
      <li>Our Animals</li>
      <li>Events</li>
      <li>Gallery</li>
      <li>Blog</li>
    </ul>
  </nav>

  <h2 class="section-title">We Love Animals</h2>
  <div class="divider dark"><span class="divider-icon" role="img" aria-label="Small sitting cat silhouette"></span></div>
</body>
</html>
```